Need a logo and business card design for my electrical company.
Company name is Kestrel Volt Electrical
In the bottow right hand corner i need
E.C. 708291 for the momument till i get my contractors license number sent to me.
Design i want black back ground with a picture of Thor's hammer and lighting hitting the top of it.

Industry/Entity Type

Electrical

Contact Information for Business Card

Owner Dermot Ashby Phone number 0412873590 email kestrelvoltelectrical@wirepostmail.com facebook page Kestrel Volt Electrical

```html
<!DOCTYPE html>
<html lang="en">
<head>
<meta charset="utf-8">
<title>Kestrel Volt Electrical – Business Card</title>
<link rel="stylesheet" href="https://fonts.googleapis.com/css2?family=Roboto+Condensed:wght@400;700&display=swap">
<style>
  :root {
    --backdrop: #e8e2d8;
    --card: #000000;
    --gold: #f2c230;
    --gold-deep: #c98f14;
    --white: #ffffff;
  }
  * { margin: 0; padding: 0; box-sizing: border-box; }
  html, body { width: 981px; height: 1200px; overflow: hidden; }
  body {
    background: var(--backdrop);
    font-family: "Roboto Condensed", Arial, sans-serif;
    position: relative;
  }
  .card {
    position: absolute;
    width: 683px;
    height: 421px;
    background: var(--card);
    overflow: hidden;
  }
  .card--front { left: 88px; top: 146px; }
  .card--back  { left: 230px; top: 638px; }

  .brand-mark {
    position: absolute;
    background: var(--gold);
  }
  .card--front .brand-mark { left: 318px; top: 98px; width: 56px; height: 56px; }
  .card--back  .brand-mark { left: 578px; top: 56px; width: 44px; height: 44px; }

  .wordmark {
    position: absolute;
    color: var(--gold);
    font-weight: 700;
    text-transform: uppercase;
    text-align: right;
    line-height: 1.02;
    letter-spacing: 0.5px;
  }
  .card--front .wordmark { right: 309px; top: 168px; font-size: 45px; }
  .card--back  .wordmark { right: 57px;  top: 114px; font-size: 32px; }

  .website {
    position: absolute;
    right: 311px;
    top: 290px;
    color: var(--white);
    font-size: 21px;
    letter-spacing: 1.8px;
  }

  .lightning-art {
    position: absolute;
    left: 402px;
    top: 0;
    width: 281px;
    height: 421px;
    background:
      radial-gradient(ellipse 45% 60% at 60% 45%, rgba(242,194,48,0.55), rgba(201,143,20,0.25) 55%, rgba(201,143,20,0) 85%),
      linear-gradient(160deg, rgba(201,143,20,0.25), rgba(0,0,0,0) 70%);
  }

  .contact { position: absolute; left: 87px; top: 118px; color: var(--white); }
  .contact__name { color: var(--gold); font-weight: 700; font-size: 23px; }
  .contact__role { font-size: 22px; margin-top: 6px; }
  .contact__list { list-style: none; margin-top: 8px; }
  .contact__item {
    display: flex; align-items: center; gap: 12px;
    font-size: 22px; height: 38px;
  }
  .contact__icon { width: 20px; height: 22px; flex: none; }

  .licence {
    position: absolute;
    right: 57px;
    top: 338px;
    color: var(--gold);
    font-size: 24px;
    letter-spacing: 0.5px;
  }
</style>
</head>
<body>
  <section class="card card--front">
    <div class="brand-mark" aria-hidden="true"></div>
    <div class="wordmark">Kestrel Volt<br>Electrical</div>
    <div class="website">www.kestrelvolt.com.au</div>
    <div class="lightning-art" role="img" aria-label="Gold lightning bolt branching down the right side of the card"></div>
  </section>

  <section class="card card--back">
    <div class="contact">
      <div class="contact__name">Dermot Ashby</div>
      <div class="contact__role">Position</div>
      <ul class="contact__list">
        <li class="contact__item">
          <svg class="contact__icon" viewBox="0 0 20 22" aria-hidden="true"><rect x="3" y="1.5" width="14" height="19" rx="2" fill="none" stroke="#f2c230" stroke-width="2"/><rect x="6" y="16" width="8" height="1.8" fill="#f2c230"/></svg>
          <span>01-2345 6789</span>
        </li>
        <li class="contact__item">
          <svg class="contact__icon" viewBox="0 0 20 22" aria-hidden="true"><rect x="1" y="5" width="18" height="12" fill="none" stroke="#f2c230" stroke-width="2"/><path d="M1 5 L10 12 L19 5" fill="none" stroke="#f2c230" stroke-width="2"/></svg>
          <span>name@company.com.au</span>
        </li>
        <li class="contact__item">
          <svg class="contact__icon" viewBox="0 0 20 22" aria-hidden="true"><path d="M10 1a7 7 0 0 0-7 7c0 5 7 13 7 13s7-8 7-13a7 7 0 0 0-7-7z" fill="#f2c230"/><circle cx="10" cy="8" r="2.6" fill="#000"/></svg>
          <span>Address</span>
        </li>
      </ul>
    </div>
    <div class="brand-mark" aria-hidden="true"></div>
    <div class="wordmark">Kestrel Volt<br>Electrical</div>
    <div class="licence">E.C. 708291</div>
  </section>
</body>
</html>
```